Brindlemark Services Ltd

I'd like to create a company letterhead for the attached logo in word format.

I'd like to emphasis the icon in large translucent state from the left corner and ensure that the letterhead colouring matches the colour palette of the current logo with a contrast so it's clear to see. I've attached a copy of our sister company page on the app for reference.

```html
<!DOCTYPE html>
<html lang="en">
<head>
<meta charset="utf-8">
<title>Brindlemark Services Ltd – Letterhead</title>
<link href="https://fonts.googleapis.com/css2?family=Lato:wght@400;700&display=swap" rel="stylesheet">
<style>
  :root {
    --board: #b5b5b5;
    --paper: #ffffff;
    --ink: #141414;
    --teal: #00b9a6;
    --teal-mist: #dff3f0;
    --label: #222222;
  }
  * { margin: 0; padding: 0; box-sizing: border-box; }
  html, body { width: 1200px; height: 850px; overflow: hidden; }
  body { background: var(--board); font-family: 'Lato', sans-serif; position: relative; }

  .letterhead {
    position: absolute; top: 115px; width: 429px; height: 606px;
    background: var(--paper); overflow: hidden;
  }
  .letterhead--teal { left: 138px; }
  .letterhead--mono { left: 611px; }
  .letterhead svg.sheet-art { position: absolute; inset: 0; }

  .company-block {
    position: absolute; top: 28px; right: 149px;
    text-align: right; font-size: 7px; line-height: 9.4px; color: #fff; letter-spacing: .1px;
  }
  .letterhead--teal .company-name { color: var(--teal); }
  .contact-block {
    position: absolute; top: 28px; left: 294px;
    font-size: 7px; line-height: 9.4px; color: #fff; letter-spacing: .1px;
  }
  .contact-row { display: flex; align-items: center; gap: 4px; }
  .contact-row svg { width: 6px; height: 6px; flex: none; }
  .letterhead--teal .contact-row svg { fill: var(--teal); }
  .letterhead--mono .contact-row svg { fill: #fff; }

  .brand-name {
    position: absolute; left: 35px; top: 84px;
    font-size: 21px; font-weight: 400; letter-spacing: .2px;
    display: flex; align-items: center; gap: 6px;
  }
  .brand-dot { width: 10px; height: 10px; border-radius: 50%; }
  .letterhead--teal .brand-name { color: var(--teal); }
  .letterhead--teal .brand-dot { background: var(--teal); }
  .letterhead--mono .brand-name { color: var(--ink); }
  .letterhead--mono .brand-dot { background: var(--ink); }

  .web-address {
    position: absolute; left: 32px; top: 585px;
    font-size: 7px; color: #fff; letter-spacing: .1px;
  }

  .sheet-label {
    position: absolute; top: 734px; width: 429px; text-align: center;
    font-size: 11px; letter-spacing: 1px; color: var(--label);
  }
  .sheet-label--one { left: 138px; }
  .sheet-label--two { left: 611px; }
</style>
</head>
<body>

<svg width="0" height="0" style="position:absolute">
  <defs>
    <radialGradient id="mist" cx="346" cy="526" r="260" gradientUnits="userSpaceOnUse">
      <stop offset="0" stop-color="#dff3f0" stop-opacity="1"/>
      <stop offset="0.45" stop-color="#e6f6f3" stop-opacity=".8"/>
      <stop offset="1" stop-color="#ffffff" stop-opacity="0"/>
    </radialGradient>
  </defs>
</svg>

<!-- Letterhead 01 -->
<div class="letterhead letterhead--teal">
  <svg class="sheet-art" viewBox="0 0 429 606" width="429" height="606">
    <rect class="brand-mist" x="110" y="300" width="319" height="306" fill="url(#mist)" role="img" aria-label="Large faint brand emblem with radiating light rays in pale teal"/>
    <path class="header-wave" fill="var(--ink)" d="M0,0 H429 V69 C400,86 368,100 328,100 C250,100 180,60 130,40 C105,30 92,26 74,26 C40,26 16,42 0,59 Z"/>
    <path class="footer-wave" fill="var(--teal)" d="M0,581 C20,572 45,568 71,568 C120,568 165,585 201,606 H0 Z"/>
  </svg>
  <div class="company-block">
    <div class="company-name">Brindlemark Services Ltd</div>
    <div>4408 Alder Crest Road</div>
    <div>Hartwell, CT 06744</div>
  </div>
  <div class="contact-block">
    <div class="contact-row"><svg viewBox="0 0 10 10"><path d="M2 0 L4 2.5 L3 3.6 C3.7 5 5 6.3 6.4 7 L7.5 6 L10 8 L8.6 10 C4 9.5 0.5 6 0 1.4 Z"/></svg>(555) 214-3870</div>
    <div class="contact-row"><svg viewBox="0 0 10 10"><path d="M2.5 0 H7.5 V3 H2.5 Z M0 3.5 H10 V8 H8 V6 H2 V8 H0 Z M2.5 6.5 H7.5 V10 H2.5 Z"/></svg>(555) 214-3871</div>
    <div class="contact-row"><svg viewBox="0 0 10 10"><path d="M0 2 H10 V3 L5 6 L0 3 Z M0 4 L5 7 L10 4 V8.5 H0 Z"/></svg>info@brindlemarkservices.com</div>
  </div>
  <div class="brand-name"><span class="brand-dot"></span>Brindlemark</div>
  <div class="web-address">www.brindlemarkservices.com</div>
</div>

<!-- Letterhead 02 -->
<div class="letterhead letterhead--mono">
  <svg class="sheet-art" viewBox="0 0 429 606" width="429" height="606">
    <rect class="brand-mist" x="110" y="300" width="319" height="306" fill="url(#mist)" role="img" aria-label="Large faint brand emblem with radiating light rays in pale teal"/>
    <path class="header-wave" fill="var(--ink)" d="M0,0 H429 V69 C400,86 368,100 328,100 C250,100 180,60 130,40 C105,30 92,26 74,26 C40,26 16,42 0,59 Z"/>
    <path class="footer-wave" fill="var(--teal)" d="M0,581 C20,572 45,568 71,568 C120,568 165,585 201,606 H0 Z"/>
  </svg>
  <div class="company-block">
    <div class="company-name">Brindlemark Services Ltd</div>
    <div>4408 Alder Crest Road</div>
    <div>Hartwell, CT 06744</div>
  </div>
  <div class="contact-block">
    <div class="contact-row"><svg viewBox="0 0 10 10"><path d="M2 0 L4 2.5 L3 3.6 C3.7 5 5 6.3 6.4 7 L7.5 6 L10 8 L8.6 10 C4 9.5 0.5 6 0 1.4 Z"/></svg>(555) 214-3870</div>
    <div class="contact-row"><svg viewBox="0 0 10 10"><path d="M2.5 0 H7.5 V3 H2.5 Z M0 3.5 H10 V8 H8 V6 H2 V8 H0 Z M2.5 6.5 H7.5 V10 H2.5 Z"/></svg>(555) 214-3871</div>
    <div class="contact-row"><svg viewBox="0 0 10 10"><path d="M0 2 H10 V3 L5 6 L0 3 Z M0 4 L5 7 L10 4 V8.5 H0 Z"/></svg>info@brindlemarkservices.com</div>
  </div>
  <div class="brand-name"><span class="brand-dot"></span>Brindlemark</div>
  <div class="web-address">www.brindlemarkservices.com</div>
</div>

<div class="sheet-label sheet-label--one">LETERHEAD 01</div>
<div class="sheet-label sheet-label--two">LETERHEAD 02</div>

</body>
</html>
```